I'm looking for strong image and design for the first book in a series titled "Theodore Pellbrook On A Voyage Through Our Convictions" subtitle "Taking Hold of Living"; although it's about beliefs, I'm not look for an ethereal feel as the first book is about how our beliefs impact our actions and expectations. I'm a published philosopher and keen on branding my name for professional purposes hence the use of my name :) The book will initially be an e-book but I will follow up with a paperback soon afterwards. My website http://theodorepellbrook-example.com/ may provide some help on me and my projects. Thanks, Theo

Target Market(s)

Graduates and corporate folk who tend to lose their way in the systems.

Logo Text

Theodore Pellbrook on Convictions

Font styles to use
Sans Serif

Colors

Designer to choose colors to be used in the design.

Requirements
Must have
• Needless to say, but impact.
Nice to have
• Strong colours
Should not have
• Religious imagery; the book is philosophical and leans into living in this world.

```html
<!DOCTYPE html>
<html lang="en">
<head>
<meta charset="utf-8">
<title>Theodore Pellbrook – A Voyage Through Our Convictions</title>
<link rel="stylesheet" href="https://fonts.googleapis.com/css2?family=Bebas+Neue&family=Playfair+Display:wght@400;500&display=swap">
<style>
  :root {
    --page-bg: #efe9ee;
    --cover-white: #ffffff;
    --ink: #151515;
    --violet: #9a2a92;
    --violet-deep: #7b2c8c;
    --cosmic-pink: #e58fcf;
    --cosmic-lilac: #a37ad6;
    --cosmic-blue: #3a3fa8;
    --text-light: #ffffff;
  }
  * { margin: 0; padding: 0; box-sizing: border-box; }
  html, body {
    width: 1200px;
    height: 1200px;
    overflow: hidden;
    background: var(--page-bg);
  }
  .book-cover {
    position: absolute;
    left: 264px;
    top: 60px;
    width: 672px;
    height: 1080px;
    background: var(--cover-white);
    overflow: hidden;
    box-shadow: 0 10px 30px rgba(60, 30, 70, 0.12);
  }
  .author-name {
    position: absolute;
    top: 44px;
    left: 0;
    width: 100%;
    text-align: center;
    font-family: "Playfair Display", serif;
    font-weight: 500;
    font-size: 27px;
    letter-spacing: 4px;
    color: var(--ink);
    text-transform: uppercase;
  }
  .title-band {
    position: absolute;
    left: 0;
    top: 223px;
    width: 615px;
    height: 74px;
  }
  .book-title {
    position: absolute;
    top: 150px;
    left: 0;
    width: 100%;
    font-family: "Bebas Neue", sans-serif;
    font-weight: 400;
    font-size: 78px;
    line-height: 74px;
    color: var(--ink);
  }
  .book-title .title-line { display: block; }
  .book-title .line-one   { padding-left: 183px; }
  .book-title .line-two   { padding-left: 218px; color: var(--text-light); }
  .book-title .line-three { padding-left: 250px; }
  .subtitle-band {
    position: absolute;
    left: 0;
    top: 460px;
    width: 100%;
    height: 80px;
    background: var(--violet);
    display: flex;
    align-items: center;
    justify-content: center;
  }
  .subtitle {
    font-family: "Playfair Display", serif;
    font-weight: 400;
    font-size: 30px;
    letter-spacing: 1px;
    color: var(--text-light);
    text-transform: uppercase;
  }
  .cover-image {
    position: absolute;
    left: 0;
    top: 540px;
    width: 100%;
    height: 540px;
    background:
      radial-gradient(ellipse at 30% 25%, rgba(240, 170, 220, 0.85), transparent 55%),
      radial-gradient(ellipse at 80% 70%, rgba(140, 110, 220, 0.8), transparent 60%),
      linear-gradient(180deg, var(--cosmic-lilac) 0%, var(--cosmic-pink) 45%, var(--cosmic-lilac) 75%, var(--cosmic-blue) 100%);
  }
</style>
</head>
<body>
  <main class="book-cover">
    <p class="author-name">Theodore Pellbrook</p>

    <svg class="title-band" viewBox="0 0 615 74" preserveAspectRatio="none" aria-hidden="true">
      <path d="M0 0 H585 L596 4 L590 10 L603 16 L594 24 L610 32 L598 40 L612 48 L597 56 L606 64 L590 70 L582 74 H0 Z" fill="var(--violet)"/>
    </svg>

    <h1 class="book-title">
      <span class="title-line line-one">A Voyage</span>
      <span class="title-line line-two">Through Our</span>
      <span class="title-line line-three">Convictions</span>
    </h1>

    <div class="subtitle-band">
      <p class="subtitle">"Taking Hold of Living"</p>
    </div>

    <div class="cover-image" role="img" aria-label="Silhouette of balanced stacked stones set against a pink and violet starry nebula sky"></div>
  </main>
</body>
</html>
```